Photography blog homepage design

I need a new webpage design for my photography blog. My blog focuses on post-processing techniques, particularly in luminosity masking, HDR photography and other advanced photo editing skills. I want the new homepage to let visitors know instantly what the blog is about as this is currently not very obvious from the feedback I received. Apart from that, the homepage should also inform/showcase latest blog post and/or popular blog post and/or some of the training courses I offer (that's my idea, but I leave it to your expertise). There should also ideally have a CTA that leads visitors to the "Start Here" page where they can learn more about my blog. The bulk of my audience is intermediate/advanced photographers who are above 30-35 years old, with a significant group in the 60 to >75 age group. The design should convey trust and creativity at the same time. The color theme for my blog is orange and dark grey. URL is www.lumivarnic.com, you can use the current content on that page.

Target Market(s)

Intermediate/advanced photographers (hobbyist or professional) age 35-75 years old.

Number of Pages Required

1 page

Font styles to use
Sans Serif

Colors
faa54b
f68e4e
f78f20

Requirements
Must have
• Upside down homepage (menus at the bottom)

```html
<!DOCTYPE html>
<html lang="en">
<head>
<meta charset="utf-8">
<title>Lumivarnic – Photo Editing Blog</title>
<link href="https://fonts.googleapis.com/css2?family=Montserrat:wght@400;500;600;700;800&display=swap" rel="stylesheet">
<style>
:root{
  --orange:#f68e4e;
  --orange-deep:#f26a2e;
  --dark:#3a3b45;
  --dark-2:#2c2d35;
  --ink:#222;
  --text:#333;
  --muted:#666;
  --teal:#0097b7;
  --line:#e2e3e6;
  --black:#000;
  --white:#fff;
}
*{box-sizing:border-box;margin:0;padding:0}
html,body{width:1200px;height:3371px;overflow:hidden}
body{position:relative;font-family:"Montserrat",sans-serif;color:var(--text);background:var(--white)}
a{text-decoration:none}

/* Hero */
.hero{position:absolute;left:0;top:0;width:1200px;height:566px;background:linear-gradient(180deg,#2f3039 0%,var(--dark) 100%);overflow:hidden}
.brand{position:absolute;left:62px;top:44px;display:flex;align-items:center;gap:12px;color:var(--white);font-weight:800;font-size:38px;letter-spacing:1px}
.brand-dot{width:30px;height:30px;border-radius:50%;background:var(--orange-deep)}
.ebook-cover{position:absolute;left:89px;top:251px;width:123px;height:185px;background:linear-gradient(160deg,#7c8794,#4d5a46 60%,#8a6a4a);box-shadow:6px 8px 14px rgba(0,0,0,.45)}
.hero-title{position:absolute;left:262px;top:194px;width:460px;color:var(--white);font-weight:800;font-size:28px;line-height:32px}
.hero-sub{position:absolute;left:262px;top:332px;width:400px;color:var(--white);font-weight:700;font-size:16.5px;line-height:21px}
.btn-orange{position:absolute;left:262px;top:438px;width:179px;height:40px;border-radius:0 20px 20px 20px;background:var(--orange-deep);color:var(--white);font-weight:700;font-size:16px;display:flex;align-items:center;padding-left:24px}
.author-photo{position:absolute;left:760px;top:131px;width:440px;height:435px;background:radial-gradient(ellipse at 55% 40%,#6b6f74 0%,#4b4d55 45%,transparent 75%)}
.hero-lines{position:absolute;left:0;top:0}

/* Published */
.published{position:absolute;left:0;top:566px;width:1200px;height:361px;background:linear-gradient(90deg,#a9abae 0%,#c9cacc 40%,#d6d7d9 100%);overflow:hidden}
.building{position:absolute;left:0;top:100px;width:260px;height:261px;background:linear-gradient(120deg,#8a8c90,#c3c4c6)}
.published h2{position:absolute;left:128px;top:56px;font-size:31px;font-weight:700;color:var(--ink);letter-spacing:.5px}
.badge{position:absolute;height:44px;border-radius:6px;background:rgba(60,60,66,.55)}

/* Help */
.help{position:absolute;left:0;top:927px;width:1200px;height:703px;background:linear-gradient(180deg,#f3f4f6,#e3e4e8)}
.help h2{position:absolute;left:0;top:60px;width:1200px;text-align:center;font-size:30px;font-weight:700;color:#333}
.card{position:absolute;top:153px;width:333px;height:465px;background:var(--white);border-radius:8px;box-shadow:0 3px 6px rgba(0,0,0,.2)}
.card-art{position:absolute;left:36px;top:34px;border-radius:6px}
.art-layers{width:112px;height:110px;background:linear-gradient(180deg,#d9dadc 0%,#9fd3ec 55%,#f6b08f 100%)}
.art-histogram{width:160px;height:90px;background:linear-gradient(90deg,#d4d5d7 0%,#c7c8ca 60%,#8fcbe8 100%)}
.art-blend{width:104px;height:104px;border-radius:50%;background:linear-gradient(135deg,#f6b08f,#9fd3ec)}
.card h3{position:absolute;left:36px;top:184px;font-size:30px;font-weight:800;line-height:30px;color:#444}
.card h3 small{display:block;font-size:23px;line-height:30px}
.card p{position:absolute;left:36px;top:267px;width:250px;font-size:16px;line-height:21px;color:#444;letter-spacing:-.3px}
.btn-teal{position:absolute;left:28px;top:379px;width:281px;height:50px;border-radius:4px;background:var(--teal);color:var(--white);font-size:17px;display:flex;align-items:center;padding-left:18px;gap:14px}

/* Story */
.story{position:absolute;left:0;top:1630px;width:1200px;height:1407px;background:var(--white)}
.avatar{position:absolute;left:139px;top:52px;width:144px;height:128px;border-radius:6px;background:linear-gradient(180deg,#e9ecef,#c9cdd2);box-shadow:0 2px 8px rgba(0,0,0,.25)}
.story-rule{position:absolute;left:315px;top:70px;width:1px;height:1212px;background:var(--line)}
.pointer{position:absolute;left:300px;top:106px;width:0;height:0;border-top:12px solid transparent;border-bottom:12px solid transparent;border-right:15px solid #bbb}
.byline{position:absolute;left:357px;top:56px}
.byline strong{display:block;font-size:17px;font-weight:500;color:var(--ink)}
.byline span{display:block;margin-top:6px;font-size:12px;color:var(--muted)}
.story-body{position:absolute;left:357px;top:148px;width:600px;font-size:16px;line-height:17.5px;color:var(--ink)}
.story-body p{margin-bottom:17.5px}
.before-after{position:absolute;left:355px;top:797px;width:603px;height:325px;background:linear-gradient(180deg,#5c6470 0%,#6f6a70 45%,#3b4357 62%,#2a3040 100%)}
.ba-split{position:absolute;left:384px;top:0;width:2px;height:325px;background:var(--white)}
.ba-handle{position:absolute;left:371px;top:149px;width:28px;height:28px;border:2px solid var(--white);border-radius:50%}
.ba-label{position:absolute;top:150px;padding:4px 12px;background:rgba(255,255,255,.15);color:var(--white);font-size:11px;letter-spacing:1px}
.cta-text{position:absolute;left:355px;top:1175px;width:600px;font-size:16px;line-height:17.5px;color:var(--ink)}
.btn-cta{position:absolute;left:353px;top:1227px;width:207px;height:47px;border-radius:3px;background:var(--teal);color:var(--white);font-size:16px;display:flex;align-items:center;padding-left:22px;gap:8px}

/* Newsletter */
.newsletter{position:absolute;left:0;top:3037px;width:1200px;height:215px;background:linear-gradient(180deg,#f1f2f4,#e2e3e7)}
.nl-title{position:absolute;left:209px;top:52px;font-size:17px;font-weight:500;color:var(--ink)}
.nl-sub{position:absolute;left:209px;top:77px;font-size:11px;color:var(--ink)}
.nl-input{position:absolute;left:209px;top:118px;width:209px;height:37px;border:1px solid #bbb;border-radius:3px;background:var(--white);font-size:15px;padding:9px 20px;color:var(--ink)}
.nl-btn{position:absolute;left:434px;top:118px;width:135px;height:37px;border-radius:3px;background:var(--dark-2);color:var(--white);font-size:15px;display:flex;align-items:center;justify-content:center}
.social-title{position:absolute;left:704px;top:54px;font-size:17px;font-weight:500;color:var(--ink)}
.social{position:absolute;top:117px;display:flex;align-items:center;gap:6px;font-size:15px;font-weight:700;color:var(--ink)}
.social i{display:block;width:10px;height:10px;border-radius:50%;background:var(--ink)}

/* Bottom menu */
.menu{position:absolute;left:0;top:3252px;width:1200px;height:119px;background:var(--black)}
.menu a{position:absolute;top:47px;color:var(--white);font-weight:800;font-size:22px;letter-spacing:.3px}
</style>
</head>
<body>

<section class="hero">
  <div class="author-photo" role="img" aria-label="Portrait photo of the blog author"></div>
  <svg class="hero-lines" width="1200" height="566" aria-hidden="true">
    <line x1="727" y1="566" x2="1200" y2="98" stroke="#fff" stroke-width="1.5"/>
    <circle cx="890" cy="403" r="31" fill="#3a3b45" stroke="#fff" stroke-width="4"/>
  </svg>
  <div class="brand"><span>LUMIVARNIC</span><span class="brand-dot"></span></div>
  <div class="ebook-cover" role="img" aria-label="Cover of the Four-Stage Edit Method ebook"></div>
  <h1 class="hero-title">Discover How To Be More Productive In Editing Without Spending More Time</h1>
  <p class="hero-sub">Download the free Four-Stage Edit Method ebook. Use the KESTREL method to boost your creativity and productivity.</p>
  <a class="btn-orange">Free Download</a>
</section>

<section class="published">
  <div class="building" role="img" aria-label="Black and white photo of a modern building"></div>
  <h2>PUBLISHED ON</h2>
  <div class="badge" style="left:132px;top:134px;width:118px;height:64px"></div>
  <div class="badge" style="left:302px;top:144px;width:144px"></div>
  <div class="badge" style="left:510px;top:132px;width:88px;height:66px"></div>
  <div class="badge" style="left:668px;top:144px;width:116px"></div>
  <div class="badge" style="left:834px;top:142px;width:188px;height:48px"></div>
  <div class="badge" style="left:132px;top:232px;width:92px;height:66px"></div>
  <div class="badge" style="left:309px;top:240px;width:130px;height:48px"></div>
  <div class="badge" style="left:530px;top:254px;width:196px;height:24px"></div>
  <div class="badge" style="left:826px;top:244px;width:210px;height:44px"></div>
</section>

<section class="help">
  <h2>WHAT DO YOU NEED HELP WITH?</h2>

  <article class="card" style="left:82px">
    <div class="card-art art-layers" role="img" aria-label="Illustration of stacked mask layers"></div>
    <h3>LUMINOSITY<small>MASKS</small></h3>
    <p>Struggling to get the right exposure? Master histograms with this ebook to help you nail the exposure in every shot.</p>
    <a class="btn-teal"><span>&#8250;</span>Mask Basics Course</a>
  </article>

  <article class="card" style="left:432px">
    <div class="card-art art-histogram" role="img" aria-label="Illustration of an image histogram"></div>
    <h3>HISTOGRAMS</h3>
    <p>Struggling to get the right exposure? Master histograms with this ebook to help you nail the exposure in every shot.</p>
    <a class="btn-teal"><span>&#8250;</span>Reading Histograms</a>
  </article>

  <article class="card" style="left:781px">
    <div class="card-art art-blend" role="img" aria-label="Illustration of blended exposures"></div>
    <h3>EXPOSURE<small>BLENDING</small></h3>
    <p>Stop producing mediocre HDR. Get the Tonal Range Plan to start creating natural looking HDR images.</p>
    <a class="btn-teal"><span>&#8250;</span>The Tonal Range Plan</a>
  </article>
</section>

<section class="story">
  <div class="avatar" role="img" aria-label="Headshot of the blog author"></div>
  <div class="pointer"></div>
  <div class="story-rule"></div>
  <div class="byline"><strong>Renwick</strong><span>Author of Lumivarnic</span></div>
  <div class="story-body">
    <p>Let me ask you this:</p>
    <p>How many cameras and lenses have you owned?</p>
    <p>I have a Vantor 24-70 f/2.8 in my inventory. I bought it from BidHub because I had read good reviews about it.</p>
    <p>But guess what...?</p>
    <p>Apart from doing some test shots, it's been sitting on my shelf collecting dust ever since.<br>I thought of selling it but never had the will to take photos, list it and all that.</p>
    <p>I also have a bunch of M42 lenses stored in another camera bag which I probably will never use them.</p>
    <p>These are just a few examples...I had even more lenses that have come and gone. Thinking back, I wasted a lot of money on gadget.</p>
    <p>As I gain more experience in photography, I learned that I don't need the best gear to produce good images...what I need is editing style!</p>
    <p>I also discovered that a good photo is 70% editing, 25% camera skills and 5% of luck!</p>
    <p>What did I change?</p>
    <p>I redirected my focus...invested more in developing a unique editing style.</p>
    <p>...and that, my friend, is one of the best decisions I have ever made!</p>
    <p>If you've been neglecting image editing...it's time to take action now and invest more effort <strong>Download The Four-Stage Edit Method to get started!.</strong></p>
  </div>
  <div class="before-after" role="img" aria-label="Before and after comparison of a frosty field at sunset">
    <div class="ba-split"></div>
    <div class="ba-handle"></div>
    <span class="ba-label" style="left:14px">Before</span>
    <span class="ba-label" style="left:528px">After</span>
  </div>
  <p class="cta-text">Want to know how to transform images like this? Click the green button below to download your free ebook!</p>
  <a class="btn-cta"><span>&#8250;</span>Get FREE ebook</a>
</section>

<section class="newsletter">
  <div class="nl-title">News &amp; Tips</div>
  <div class="nl-sub">Sign up to receive our latest reviews.</div>
  <div class="nl-input">Email</div>
  <div class="nl-btn">Subscribe</div>
  <div class="social-title">Stay tuned</div>
  <div class="social" style="left:707px"><i></i>Pixdrift</div>
  <div class="social" style="left:800px"><i></i>Chirper</div>
  <div class="social" style="left:884px"><i></i>Snapgram</div>
  <div class="social" style="left:990px"><i></i>Friendwall</div>
</section>

<nav class="menu">
  <a style="left:310px">START HERE</a>
  <a style="left:508px">BLOG</a>
  <a style="left:627px">TUTORIALS</a>
  <a style="left:805px">ABOUT</a>
</nav>

</body>
</html>
```